Want to fly? Flight school needs a roll up

Hello designers

We are a small aviation club with around 100 members. We love flying and therefore offer free flight lessons for young people at our glider flight school.
The young people only have to pay a flat rate of €300 for the aircraft until their first solo flight.
To advertise the flight school we now need a roll up banner measuring 85cm x 200cm. You can find the data sheet for the banner in the appendix.
Content of the roll up banner:
Advertising for our flight school so that we can attract new members
The banner should be designed in our club colors blue/white
The banner is aimed at all people who want to get a glider license
A great offer for young people up to the age of 25 should be placed on the banner with a reference to the text “Offer only applies to people up to the age of 25. Included in the flat rate of €300 is training on the glider up to the first "solo flight"
The banner is intended to advertise training with a glider. Therefore the wish would be for a glider to be depicted

Here is a link to our current homepage

https://www.lsg-tarnhofen.de/

https://www.vidoplex.example/watch?v=K8p2Qz4LmXc

Target Market(s)

Young people from 14 years to 30 years

Colors
0054AA
0677BA
7BADD7
CADEEF
E8F1F8

Requirements
Nice to have
• Glider / club logo
Should not have
• Too much text

```html
<!DOCTYPE html>
<html lang="en">
<head>
<meta charset="utf-8">
<title>Luftsportgruppe Tarnhofen – Flight School Roll-up</title>
<link rel="stylesheet" href="https://fonts.googleapis.com/css2?family=Raleway:wght@600;700;800&display=swap">
<style>
  :root {
    --navy: #2b3590;
    --mid-blue: #1b5aa8;
    --club-blue: #0677ba;
    --sky-blue: #2aa7e0;
    --light-blue: #7badd7;
    --pale-blue: #cadeef;
    --white: #ffffff;
    --text-navy: #2a3389;
  }
  html, body {
    margin: 0;
    padding: 0;
    overflow: hidden;
    background: var(--white);
  }
  .banner {
    position: relative;
    width: 1200px;
    height: 2824px;
    overflow: hidden;
    font-family: "Raleway", Arial, sans-serif;
  }
  .banner__shapes {
    position: absolute;
    inset: 0;
    width: 1200px;
    height: 2824px;
  }
  .club-name {
    position: absolute;
    left: 110px;
    top: 150px;
    display: flex;
    align-items: center;
    gap: 22px;
    color: var(--text-navy);
    font-weight: 800;
    font-size: 42px;
    line-height: 1.1;
  }
  .club-name__dot {
    width: 60px;
    height: 60px;
    border-radius: 50%;
    background: var(--text-navy);
    flex: none;
  }
  .headline {
    position: absolute;
    left: 0;
    right: 0;
    top: 976px;
    margin: 0;
    text-align: center;
    color: var(--white);
    font-weight: 700;
    font-size: 106px;
    line-height: 127px;
  }
  .offer {
    position: absolute;
    left: 150px;
    right: 150px;
    top: 1540px;
    margin: 0;
    text-align: center;
    color: var(--white);
  }
  .offer__main {
    display: block;
    font-weight: 800;
    font-size: 38px;
    line-height: 50px;
  }
  .offer__note {
    display: block;
    margin-top: 10px;
    color: var(--pale-blue);
    font-weight: 600;
    font-size: 24px;
    line-height: 32px;
  }
  .web-address {
    position: absolute;
    left: 0;
    right: 0;
    top: 2682px;
    margin: 0;
    text-align: center;
    color: var(--text-navy);
    font-weight: 800;
    font-size: 54px;
    line-height: 70px;
  }
</style>
</head>
<body>
<main class="banner">
  <svg class="banner__shapes" viewBox="0 0 1200 2824" xmlns="http://www.w3.org/2000/svg">
    <defs>
      <radialGradient id="mainGlow" cx="600" cy="1320" r="1000" gradientUnits="userSpaceOnUse">
        <stop offset="0" stop-color="#1f6cb8"/>
        <stop offset="0.6" stop-color="#2550a2"/>
        <stop offset="1" stop-color="#2b3590"/>
      </radialGradient>
      <linearGradient id="sceneTones" x1="0" y1="1750" x2="0" y2="2440" gradientUnits="userSpaceOnUse">
        <stop offset="0" stop-color="#6e9bc8"/>
        <stop offset="0.3" stop-color="#c3dad8"/>
        <stop offset="0.55" stop-color="#72c6cf"/>
        <stop offset="0.78" stop-color="#3c6b82"/>
        <stop offset="1" stop-color="#2f5230"/>
      </linearGradient>
    </defs>

    <rect class="scene" x="0" y="1700" width="1200" height="760" fill="url(#sceneTones)"
          role="img" aria-label="Photo of a glider approaching a grass airfield with mountains and trees under a cloudy sky"/>

    <path class="main-field" d="M0,0 H1200 V1752 Q600,1990 0,1752 Z" fill="url(#mainGlow)"/>

    <path class="top-band-dark" d="M0,625 Q900,600 1200,70 L1200,0 L690,0 Q640,520 0,560 Z" fill="var(--mid-blue)"/>
    <path class="top-band-light" d="M690,0 L1200,0 L1200,40 Q1000,380 560,420 Q670,250 690,0 Z" fill="var(--club-blue)"/>
    <path class="top-white" d="M0,0 L706,0 Q650,530 0,558 Z" fill="var(--white)"/>

    <path class="flight-path" d="M590,300 Q1110,520 1200,980" fill="none" stroke="var(--white)" stroke-width="3" stroke-dasharray="9 8"/>
    <path class="flight-path flight-path--sky" d="M0,1120 Q110,1700 700,2200 Q950,2420 1200,2570" fill="none" stroke="var(--sky-blue)" stroke-width="5" stroke-dasharray="22 14"/>

    <path class="bottom-left" d="M0,2280 Q420,2285 640,2425 L0,2824 Z" fill="#1a4fa0"/>
    <path class="bottom-right" d="M1200,2298 Q800,2295 580,2425 L1200,2824 Z" fill="var(--club-blue)"/>
    <path class="bottom-white" d="M0,2824 Q170,2500 612,2418 Q1040,2500 1200,2824 Z" fill="var(--white)"/>

    <g class="web-icon" fill="none" stroke="var(--text-navy)" stroke-width="14">
      <circle cx="608" cy="2560" r="72"/>
      <ellipse cx="608" cy="2560" rx="28" ry="72"/>
      <line x1="536" y1="2560" x2="680" y2="2560"/>
      <line x1="550" y1="2524" x2="666" y2="2524"/>
      <line x1="550" y1="2596" x2="666" y2="2596"/>
    </g>
    <path class="web-icon-pointer" d="M628,2572 L652,2656 L664,2628 L690,2654 L704,2640 L678,2614 L708,2602 Z"
          fill="var(--text-navy)" stroke="var(--white)" stroke-width="7" stroke-linejoin="round"/>
  </svg>

  <div class="club-name">
    <span class="club-name__dot"></span>
    <span>Luftsportgruppe<br>Tarnhofen e.V.</span>
  </div>

  <h1 class="headline">Join our<br>flight school<br>and get a glider<br>license</h1>

  <p class="offer">
    <span class="offer__main">Up to age 25: only €300 flat rate</span>
    <span class="offer__note">Offer only applies to people up to the age of 25. Included in the flat rate of €300 is training on the glider up to the first "solo flight".</span>
  </p>

  <p class="web-address">www.lsg-tarnhofen.de</p>
</main>
</body>
</html>
```